Brovik Pty Ltd business card design

We need a business card for our company who is involved in upper market residential property development.
Design should be elegant and contemporary.

Our residences are inspired and elegant in contemporary design, combined with inviting ambience. We produce exclusive boutique developments which appeal to the most discerning of purchasers.
We would like to see a design to reflect the above.
Updates

Industry/Entity Type

Residential

Contact Information for Business Card

Brovik Pty Ltd, Marco Sidlewski, PO Box 58 Larkdale 3190 Melbourne AUSTRALIA, ph (+61 3) 0427 5096 82

Logo Text

Brovik Pty Ltd

```html
<!DOCTYPE html>
<html lang="en">
<head>
<meta charset="utf-8">
<title>Brovik Pty Ltd – Business Card</title>
<link rel="stylesheet" href="https://fonts.googleapis.com/css2?family=Open+Sans:wght@400;600;700&display=swap">
<style>
  :root {
    --stage: #0c0c0d;
    --card: #1d1d1f;
    --card-deep: #141415;
    --brand-blue: #0a5a9e;
    --paper-white: #f4f4f4;
    --text-white: #ffffff;
  }
  * { margin: 0; padding: 0; box-sizing: border-box; }
  html, body {
    width: 1200px;
    height: 900px;
    overflow: hidden;
    background: var(--stage);
    font-family: "Open Sans", Arial, sans-serif;
  }
  .canvas {
    position: relative;
    width: 1200px;
    height: 900px;
  }
  .card {
    position: absolute;
    width: 560px;
    height: 340px;
    border-radius: 10px;
    overflow: hidden;
    background: linear-gradient(160deg, var(--card) 0%, var(--card-deep) 100%);
    box-shadow: 0 18px 40px rgba(0, 0, 0, 0.6);
  }
  .card--back { left: 560px; top: 90px; }
  .card--front { left: 80px; top: 470px; }
  .card__wave {
    position: absolute;
    inset: 0;
    width: 100%;
    height: 100%;
  }
  .wave-blue { fill: var(--brand-blue); }
  .wave-white { fill: var(--paper-white); }

  .company-name {
    position: absolute;
    left: 0;
    top: 146px;
    width: 460px;
    text-align: center;
    color: var(--text-white);
    font-weight: 700;
    font-size: 34px;
    letter-spacing: 3px;
  }

  .contact {
    position: absolute;
    left: 190px;
    top: 82px;
    color: var(--text-white);
  }
  .contact__name {
    color: var(--brand-blue);
    font-weight: 400;
    font-size: 21px;
    letter-spacing: 1px;
    margin-bottom: 12px;
  }
  .contact__line {
    font-weight: 600;
    font-size: 16px;
    line-height: 24px;
    letter-spacing: 0.5px;
  }
  .contact__label { color: var(--brand-blue); }
</style>
</head>
<body>
<main class="canvas">

  <section class="card card--back" aria-label="Business card, contact side">
    <svg class="card__wave" viewBox="0 0 560 340" aria-hidden="true">
      <path class="wave-blue" d="M515 0 C505 110 470 170 430 230 C405 270 392 305 388 340 L515 340 L536 0 Z"/>
      <path class="wave-white" d="M536 0 L556 0 L534 340 L512 340 Z"/>
    </svg>
    <div class="contact">
      <p class="contact__name">Marco Sidlewski</p>
      <p class="contact__line">PO Box 58 Larkdale 3190</p>
      <p class="contact__line">Melbourne AUSTRALIA.</p>
      <p class="contact__line"><span class="contact__label">ph</span> (+61 3) 0427 5096 82</p>
    </div>
  </section>

  <section class="card card--front" aria-label="Business card, company side">
    <svg class="card__wave" viewBox="0 0 560 340" aria-hidden="true">
      <path class="wave-blue" d="M515 0 C505 110 470 170 430 230 C405 270 392 305 388 340 L515 340 L536 0 Z"/>
      <path class="wave-white" d="M536 0 L556 0 L534 340 L512 340 Z"/>
    </svg>
    <h1 class="company-name">Brovik Pty Ltd</h1>
  </section>

</main>
</body>
</html>
```